Business Card Design needed for logo design project

Our business needs a business card design. I'm not sure what format files are generally delivered back, but clearly I will need the ability to edit to add colleagues contact details.

Our logo is attached.

Brivanor is a 3D design services company, providing app, serious/educational game, VR and AR websites/applications to corporate clients.

Target Market(s)

Corporate blue-chip clients needing 3D design services

Industry/Entity Type

Business

Font styles to use
Sans Serif

Requirements
Must have
• Templated such that I can add details (name, phone number etc). Needs to include logo from previous project winner - attached.

```html
<!DOCTYPE html>
<html lang="en">
<head>
<meta charset="utf-8">
<title>Brivanor – Business Card</title>
<link rel="stylesheet" href="https://fonts.googleapis.com/css2?family=Open+Sans:wght@400;600&display=swap">
<style>
  :root {
    --red: #e91d29;
    --red-dark: #a51c22;
    --white: #ffffff;
    --ink: #3a3a3c;
    --backdrop: #c9c9c9;
  }
  * { margin: 0; padding: 0; box-sizing: border-box; }
  html, body {
    width: 1200px;
    height: 900px;
    overflow: hidden;
  }
  body {
    background: var(--backdrop);
    font-family: "Open Sans", sans-serif;
    display: flex;
    flex-direction: column;
    align-items: center;
    justify-content: center;
    gap: 44px;
  }
  .card {
    position: relative;
    width: 588px;
    height: 336px;
    overflow: hidden;
    box-shadow: 0 6px 18px rgba(0, 0, 0, 0.18);
  }
  .card--front { background: var(--red); }
  .card--back { background: var(--white); }

  .wordmark {
    position: absolute;
    left: 0;
    right: 0;
    display: flex;
    align-items: center;
    justify-content: center;
    gap: 14px;
  }
  .card--front .wordmark { top: 50%; transform: translateY(-50%); }
  .card--back .wordmark { top: 60px; }

  .wordmark__dot {
    width: 50px;
    height: 50px;
    border-radius: 50%;
  }
  .wordmark__name {
    font-size: 40px;
    font-weight: 400;
    letter-spacing: 4px;
    text-transform: uppercase;
    line-height: 1;
  }
  .card--front .wordmark__dot { background: var(--white); }
  .card--front .wordmark__name { color: var(--white); }
  .card--back .wordmark__dot { background: var(--red); }
  .card--back .wordmark__name { color: var(--ink); }

  .card__circles {
    position: absolute;
    inset: 0;
  }
  .circle--left { fill: var(--red-dark); }
  .circle--right { fill: var(--red); }

  .contact {
    position: absolute;
    color: var(--white);
    font-size: 14px;
    line-height: 1.4;
    letter-spacing: 0.3px;
  }
  .contact--left { left: 24px; top: 228px; }
  .contact--right { right: 24px; top: 264px; text-align: right; }
</style>
</head>
<body>

  <section class="card card--front" aria-label="Business card front">
    <div class="wordmark">
      <span class="wordmark__dot"></span>
      <span class="wordmark__name">Brivanor</span>
    </div>
  </section>

  <section class="card card--back" aria-label="Business card back">
    <svg class="card__circles" viewBox="0 0 588 336" width="588" height="336" aria-hidden="true">
      <defs>
        <filter id="circle-shadow" x="-20%" y="-20%" width="140%" height="140%">
          <feDropShadow dx="-3" dy="0" stdDeviation="4" flood-color="#000" flood-opacity="0.3"/>
        </filter>
      </defs>
      <circle class="circle--left" cx="150" cy="322" r="178"/>
      <circle class="circle--right" cx="424" cy="358" r="172" filter="url(#circle-shadow)"/>
    </svg>

    <div class="wordmark">
      <span class="wordmark__dot"></span>
      <span class="wordmark__name">Brivanor</span>
    </div>

    <p class="contact contact--left">
      E-mail: hello@brivanor.net<br>
      Tel: 555 014
    </p>
    <p class="contact contact--right">
      Web: brivanor.net<br>
      Fax: 555 014 7
    </p>
  </section>

</body>
</html>
```